Business Card Design Project

Business Card
We are rebranding with a new logo
Industry/Entity Type
Business
Contact Information for Business Card
Dennis Marlow +61 427581962 dennis@qovo.com.au P.O. Box 872 Kelvindale QLD 4309
Requirements
Must have
- Logo

```html
<!DOCTYPE html>
<html lang="en">
<head>
<meta charset="utf-8">
<title>Qovo International — Business Card</title>
<link rel="stylesheet" href="https://fonts.googleapis.com/css2?family=Barlow:wght@500;600&display=swap">
<style>
  :root {
    --page-bg: #e7e4df;
    --card-bg: #fbfbfa;
    --brand-blue: #1b6990;
    --ink-blue: #1f4d6b;
    --brand-orange: #e8731f;
    --card-shadow: rgba(40, 30, 20, 0.25);
  }
  * { margin: 0; padding: 0; box-sizing: border-box; }
  html, body {
    width: 1200px;
    height: 675px;
    overflow: hidden;
    background: var(--page-bg);
    font-family: "Barlow", Arial, sans-serif;
  }
  .card {
    position: absolute;
    left: 80px;
    top: 42px;
    width: 1040px;
    height: 590px;
    background: linear-gradient(160deg, #ffffff 0%, var(--card-bg) 60%, #f3f3f1 100%);
    border-bottom: 9px solid var(--brand-orange);
    box-shadow: 0 6px 18px var(--card-shadow);
  }
  .holder-name {
    position: absolute;
    left: 62px;
    top: 44px;
    font-size: 74px;
    font-weight: 600;
    color: var(--brand-blue);
    letter-spacing: 0.5px;
    line-height: 1;
  }
  .contact-line {
    position: absolute;
    left: 62px;
    display: flex;
    align-items: center;
    gap: 14px;
    font-size: 40px;
    font-weight: 500;
    color: var(--brand-orange);
    line-height: 1;
  }
  .contact-phone { top: 136px; }
  .contact-email { top: 192px; }
  .contact-icon {
    width: 32px;
    height: 32px;
    flex: none;
    fill: var(--brand-blue);
  }
  .contact-at {
    width: 32px;
    flex: none;
    color: var(--brand-blue);
    font-size: 38px;
    text-align: center;
  }
  .brand-name {
    position: absolute;
    left: 87px;
    top: 410px;
    display: flex;
    align-items: center;
    gap: 14px;
    color: var(--brand-blue);
    font-weight: 600;
  }
  .brand-dot {
    width: 28px;
    height: 28px;
    border-radius: 50%;
    background: var(--brand-orange);
    flex: none;
  }
  .brand-words { line-height: 1; }
  .brand-main { display: block; font-size: 64px; }
  .brand-sub { display: block; font-size: 20px; letter-spacing: 4px; margin-top: 8px; text-transform: uppercase; }
  .divider {
    position: absolute;
    left: 363px;
    top: 444px;
    width: 3px;
    height: 86px;
    background: var(--brand-orange);
  }
  .postal-address {
    position: absolute;
    left: 400px;
    top: 470px;
    font-size: 34px;
    font-weight: 500;
    color: var(--ink-blue);
    letter-spacing: 0.4px;
    font-style: normal;
  }
</style>
</head>
<body>
  <main class="card">
    <h1 class="holder-name">Dennis Marlow</h1>

    <p class="contact-line contact-phone">
      <svg class="contact-icon" viewBox="0 0 24 24" aria-hidden="true">
        <path d="M6.6 10.8c1.4 2.8 3.8 5.1 6.6 6.6l2.2-2.2c.3-.3.7-.4 1-.2 1.1.4 2.3.6 3.6.6.6 0 1 .4 1 1V20c0 .6-.4 1-1 1C10.6 21 3 13.4 3 4c0-.6.4-1 1-1h3.5c.6 0 1 .4 1 1 0 1.3.2 2.5.6 3.6.1.3 0 .7-.2 1l-2.3 2.2z"/>
      </svg>
      <span>+61 427581962</span>
    </p>

    <p class="contact-line contact-email">
      <span class="contact-at">@</span>
      <span>dennis@qovo.com.au</span>
    </p>

    <div class="brand-name">
      <span class="brand-dot" aria-hidden="true"></span>
      <span class="brand-words">
        <span class="brand-main">Qovo</span>
        <span class="brand-sub">International</span>
      </span>
    </div>

    <span class="divider" aria-hidden="true"></span>

    <address class="postal-address">P.O. Box 872 Kelvindale QLD 4309</address>
  </main>
</body>
</html>
```